TalkWell Needs a Business Card

We need a business card for Tomas Ferreby, Ph.D., CCC-SLP, who is affiliated with Hollander Ridge University. He is an Associate Professor and Licensed Speech-Language Pathologist, Department of Communication Disorders, College of Health and Human Services.

He has a consulting business "TalkWell Consultant". The logo is attached. The consulting company color is Turquoise. HRU school color is orange.

The consulting business focus on: Consultation, Research & Professional Development. Our target market is individuals with annual family income of $100,000.00 or more for consultation and speech-language pathologists for professional development activities.

No harsh colors, subtle colors appreciated. Address, e-mail, telephone, and small scan logo for a link to our website. Creativity in design will be appreciated. Please add your comments, why you created this design?

Thanks and looking for submissions.

```html
<!DOCTYPE html>
<html lang="en">
<head>
<meta charset="utf-8">
<title>TalkWell Consultants – Business Card</title>
<link href="https://fonts.googleapis.com/css2?family=Open+Sans:wght@400;600&display=swap" rel="stylesheet">
<style>
  :root {
    --backdrop: #3b3d41;
    --card: #ffffff;
    --turquoise: #5cc8d0;
    --leaf: #4fb848;
  }
  * { margin: 0; padding: 0; box-sizing: border-box; }
  html, body {
    width: 1037px;
    height: 1200px;
    overflow: hidden;
    background: var(--backdrop);
    font-family: "Open Sans", sans-serif;
  }
  .canvas { position: relative; width: 1037px; height: 1200px; }
  .card {
    position: absolute;
    left: 187px;
    width: 705px;
    height: 398px;
    background: var(--card);
    overflow: hidden;
  }
  .card--front { top: 120px; }
  .card--back { top: 649px; }

  .brand { display: flex; align-items: center; color: var(--turquoise); font-weight: 400; }
  .brand__dot { border-radius: 50%; background: var(--turquoise); flex: none; }

  .card--front .brand {
    position: absolute;
    left: 0; right: 0; top: 0; bottom: 0;
    justify-content: center;
    gap: 26px;
    font-size: 54px;
  }
  .card--front .brand__dot { width: 96px; height: 96px; }

  .card--back .brand {
    position: absolute;
    left: 45px;
    top: 98px;
    gap: 22px;
    font-size: 38px;
  }
  .card--back .brand__dot { width: 78px; height: 78px; }

  .corner { position: absolute; top: 0; left: 0; width: 705px; height: 398px; }

  .holder {
    position: absolute;
    left: 43px;
    top: 282px;
    color: var(--turquoise);
    font-size: 26px;
    font-weight: 600;
  }
  .holder__credentials { font-size: 17px; font-weight: 400; }
  .holder-rule {
    position: absolute;
    left: 43px;
    top: 328px;
    width: 549px;
    height: 2px;
    background: var(--turquoise);
  }
  .contact {
    position: absolute;
    left: 43px;
    top: 342px;
    color: var(--leaf);
    font-size: 18px;
  }
</style>
</head>
<body>
<main class="canvas">
  <section class="card card--front">
    <div class="brand">
      <span class="brand__dot"></span>
      <span class="brand__name">TalkWell Consultants</span>
    </div>
  </section>

  <section class="card card--back">
    <svg class="corner" viewBox="0 0 705 398" aria-hidden="true">
      <polygon points="434,0 705,0 705,277" fill="var(--turquoise)"/>
      <line x1="416" y1="0" x2="705" y2="292" stroke="var(--leaf)" stroke-width="5"/>
      <circle cx="612" cy="92" r="38" fill="#ffffff"/>
    </svg>
    <div class="brand">
      <span class="brand__dot"></span>
      <span class="brand__name">TalkWell Consultants</span>
    </div>
    <p class="holder">Tomas Ferreby<span class="holder__credentials">, Ph.D., CCC-SLP</span></p>
    <div class="holder-rule"></div>
    <p class="contact">phone number, email, website</p>
  </section>
</main>
</body>
</html>
```